Tequila Velmaros Web Design Project

We are launching a new Ultra Premium Tequila; the brand name is "Velmaros".
Velmaros was the colloquial name given to Spanish immigrants that came to America in the 19th and early part of the 20th centuries, made fortune and went back to Spain to propel even greater opportunities for those in their homeland, started banks, built schools, roads, built eclectic houses, some acquired noble titles, they were brazen, altruist and built a better world along the way.
Our product is 100% Blue Agave and will have the 4 types of tequila: Silver, Reposado, Añejo and Extra Añejo.
Updates

Dear All,
I have attached some more information/content for your review.
Kind Regards,

After some consideration, we have decided to include our line of Premium Margaritas on the same site.
Our Margaritas are made with 100% Blue Agave Silver Tequila and lightly sweetened with Agave Nectar.
Please see file with the 5 different flavors available.
Thank you,

Target Market(s)

Our target market is affluent people, especially Hispanics, because most of the have a Spanish heritage and/or ancestry; also, entrepreneurs of today.

Industry/Entity Type

Product

Requirements
Must have
• We will provide pictures and content/text for the pages.

```html
<!DOCTYPE html>
<html lang="en">
<head>
<meta charset="utf-8">
<title>Tequila Velmaros</title>
<link rel="stylesheet" href="https://fonts.googleapis.com/css2?family=PT+Sans:ital,wght@0,400;0,700;1,400&family=Italianno&family=Lora&display=swap">
<style>
:root{
  --wood-light:#f6dfb3;
  --wood-mid:#ecca8e;
  --panel:#fafaf8;
  --panel-line:#e3e3e0;
  --ink:#4a4a4a;
  --ink-soft:#5c5c5c;
  --amber:#d8963a;
  --amber-dark:#b9771f;
  --btn-top:#e9ae56;
  --btn-bot:#d4922f;
  --nav-top:#4b4b4b;
  --nav-bot:#2b2b2b;
  --dark:#414141;
  --field-top:#f7f7f7;
  --field-bot:#e4e4e4;
  --white:#ffffff;
}
*{box-sizing:border-box;margin:0;padding:0}
html,body{width:993px;height:1200px;overflow:hidden}
body{
  position:relative;
  font-family:"PT Sans",sans-serif;
  color:var(--ink);
  background:repeating-linear-gradient(90deg,var(--wood-light) 0 7px,var(--wood-mid) 7px 9px,var(--wood-light) 9px 19px,#f0d49f 19px 22px);
}
a{text-decoration:none}
.abs{position:absolute}
.script{font-family:"Italianno",cursive;font-weight:400;color:#3b3b3b;line-height:1;word-spacing:4px}

/* header */
.site-header{left:99px;top:21px;width:795px;height:109px;background:var(--white);border-radius:4px;box-shadow:0 1px 3px rgba(0,0,0,.18)}
.brand{left:13px;top:10px;width:146px;height:89px;display:flex;align-items:center;gap:8px}
.brand-mark{width:14px;height:14px;background:var(--amber);border-radius:50%}
.brand-name{font-size:24px;font-weight:700;color:var(--amber-dark);letter-spacing:.5px}
.call{right:9px;top:20px;font-size:16px;color:#333;white-space:nowrap}
.call strong{font-weight:400;font-size:21px;color:var(--amber);letter-spacing:.5px}
.main-nav{left:191px;top:65px;width:596px;height:31px;display:flex;border-radius:3px;overflow:hidden;background:linear-gradient(var(--nav-top),var(--nav-bot))}
.main-nav a{display:flex;align-items:center;justify-content:center;color:#f0f0f0;font-size:12px;border-right:1px solid #1f1f1f;box-shadow:inset -1px 0 0 #555}
.main-nav a:last-child{border:0;box-shadow:none}
.main-nav a.active{background:linear-gradient(var(--btn-top),var(--btn-bot))}

/* main panel */
.main-panel{left:99px;top:145px;width:795px;height:737px;background:var(--panel);border-radius:4px;box-shadow:0 1px 3px rgba(0,0,0,.18)}
.welcome-title{left:15px;top:14px;font-size:34px}
.photo{background:linear-gradient(#a9b2ae 0%,#6f7a63 30%,#3e4a38 60%,#2d3424 100%);border:3px solid var(--white);box-shadow:0 0 0 1px #d8d8d8}
.welcome-photo{left:17px;top:49px;width:340px;height:134px}
.welcome-text{left:15px;top:197px;width:345px;font-size:10.5px;line-height:16.5px;color:var(--ink-soft)}
.btn{display:flex;align-items:center;justify-content:center;background:linear-gradient(var(--btn-top),var(--btn-bot));color:var(--white);border-radius:3px;box-shadow:0 2px 0 #a86e1e}
.more-btn{left:300px;top:382px;width:57px;height:28px;font-size:11.5px;font-weight:700;color:#3a2a14}

.showcase{left:406px;top:11px;width:381px;height:398px;background:radial-gradient(circle at 60% 45%,#fdfdfd,#e6e6e6 80%);border-radius:4px;box-shadow:0 14px 14px -10px rgba(0,0,0,.35)}
.bottle-shot{left:100px;top:12px;width:120px;height:376px;background:linear-gradient(180deg,#d9d2c2 0%,#e2b55a 30%,#d99a26 70%,#e6e3dc 100%)}
.tagline{right:10px;top:46px;text-align:right;font-size:30px;line-height:31px;color:#333}
.tagline .hl{color:#9a4a1a;font-size:40px}
.thumb-rail{left:393px;top:39px;width:91px;height:318px;background:linear-gradient(90deg,#fafafa,#e9e9e9);border-radius:4px;box-shadow:0 2px 4px rgba(0,0,0,.25)}
.thumb{left:5px;width:81px;height:65px;border:3px solid var(--white);box-shadow:0 0 0 1px #cfcfcf;background:var(--c)}
.thumb.active{box-shadow:0 0 0 2px var(--amber)}
.rail-arrow{left:40px;width:12px;height:8px}

.divider{left:8px;top:443px;width:779px;height:3px;background:var(--panel-line)}
.feature{top:468px;width:240px}
.feature h2{font-size:33px}
.feature .photo{position:relative;margin-top:6px;width:237px;height:124px;background:linear-gradient(110deg,#6b4a2c,#b08462 40%,#e7e1d8 55%,#4d3a2a)}
.feature p{margin-top:17px;font-size:10.5px;line-height:16.5px;color:var(--ink-soft);width:240px}
.feature a{display:block;margin-top:9px;font-size:12px;font-weight:700;color:var(--amber)}
.play{position:absolute;left:100px;top:40px;width:36px;height:36px}

/* footer panel */
.contact-bar{left:99px;top:897px;width:795px;height:249px;background:var(--dark);border-radius:3px}
.contact-bar h3{color:var(--white);font-size:33px}
.quick{left:15px;top:10px}
.field{left:15px;width:234px;height:25px;background:linear-gradient(var(--field-top),var(--field-bot));border:1px solid #bfbfbf;font-size:11px;color:#444;padding:6px 8px}
.submit{left:191px;top:209px;width:58px;height:24px;font-size:11px;box-shadow:none}
.news{left:297px;top:10px}
.news-item{left:297px;width:240px;height:60px}
.date{position:absolute;left:0;top:0;font-family:"Lora",serif;color:var(--btn-top);font-size:31px;line-height:1}
.date small{font-size:21px}
.news-item p{position:absolute;left:84px;top:2px;width:150px;font-size:10.5px;line-height:17px;color:#eee}
.news-item a{position:absolute;left:84px;top:44px;font-size:10.5px;color:var(--btn-top);text-decoration:underline}
.news-rule{left:297px;top:114px;width:233px;height:1px;background:#6a6a6a}
.testi{left:556px;top:10px}
.quote-mark{left:551px;top:40px;width:34px;height:34px}
.testi-text{left:567px;top:56px;width:215px;font-size:10.5px;line-height:17.5px;font-style:italic;color:#eee;text-indent:30px}
.testi-text a{color:var(--btn-top)}
.avatar{left:714px;top:151px;width:65px;height:65px;background:linear-gradient(#d9c2a6,#8d5e4a);border:3px solid var(--white)}
.author{right:91px;top:192px;text-align:right;font-size:10.5px;color:var(--btn-top);line-height:16px}
.author span{display:block;font-size:9px;font-style:italic;color:#aaa}

/* bottom */
.legal{left:108px;top:1167px;font-size:10.5px;color:#444}
.social{left:751px;top:1156px;display:flex;gap:6px}
.social span{width:29px;height:29px;border-radius:50%;background:#2e2e2e}
</style>
</head>
<body>

<header class="site-header abs">
  <div class="brand abs"><span class="brand-mark"></span><span class="brand-name">Velmaros</span></div>
  <div class="call abs">Call Us : <strong>123 555 0190</strong></div>
  <nav class="main-nav abs">
    <a class="active" href="#" style="width:61px">Home</a>
    <a href="#" style="width:76px">About Us</a>
    <a href="#" style="width:104px">Tequila Maker</a>
    <a href="#" style="width:115px">Press &amp; Reviews</a>
    <a href="#" style="width:58px">Order</a>
    <a href="#" style="width:96px">Testimonials</a>
    <a href="#" style="width:86px">Contact Us</a>
  </nav>
</header>

<main class="main-panel abs">
  <h1 class="welcome-title script abs">Welcome to Our Site</h1>
  <div class="welcome-photo photo abs" role="img" aria-label="Agave field with a worker harvesting under mountains"></div>
  <p class="welcome-text abs">Lorem ipsum dolor sit amet, consectetur adipiscing elit. Fusce accum-san, elit a suscipit sagittis, tortor sapien cursus risus, non rhoncus lectus nunc ac nulla.<br>Aliquam molestie, mi et imperdiet euismod, dui purus auctor tellus, et interdum lacus lectus et ante. Sed accumsan sollicitudin sapien, sit amet adipiscing turpis gravida ac. In congue, neque ac lobortis volutpat, libero mauris varius mi, vitae suscipit ipsum ligula vitae risus. Duis aliquam nibh a dui iaculis viverra id a velit. Vivamus egestas risus in magna varius commodo. Sed semper viverra egestas. Etiam pretium porttitor lectus, vel ornare neque porta volutpat.</p>
  <a class="more-btn btn abs" href="#">MORE</a>

  <section class="showcase abs">
    <div class="bottle-shot abs" role="img" aria-label="Product photo of the añejo tequila bottle"></div>
    <p class="tagline script abs">We are a<br>Maker of Best<br><span class="hl">Tequila</span><br>for our<br>Customers</p>
  </section>

  <div class="thumb-rail abs">
    <svg class="rail-arrow abs" style="top:6px" viewBox="0 0 12 8"><path d="M2 6l4-4 4 4" fill="none" stroke="#555" stroke-width="1.5"/></svg>
    <div class="thumb abs" style="top:22px;--c:linear-gradient(#faf7f0,#ecd7a8)" role="img" aria-label="Silver tequila bottle"></div>
    <div class="thumb active abs" style="top:94px;--c:linear-gradient(#f5f1e6,#e7c16f)" role="img" aria-label="Añejo tequila bottle"></div>
    <div class="thumb abs" style="top:164px;--c:linear-gradient(#f3ede2,#e0a64a)" role="img" aria-label="Reposado tequila bottle"></div>
    <div class="thumb abs" style="top:234px;--c:linear-gradient(#f4f4f4,#bdbdbd)" role="img" aria-label="Extra añejo tequila bottle"></div>
    <svg class="rail-arrow abs" style="top:304px" viewBox="0 0 12 8"><path d="M2 2l4 4 4-4" fill="none" stroke="#555" stroke-width="1.5"/></svg>
  </div>

  <div class="divider abs"></div>

  <article class="feature abs" style="left:15px">
    <h2 class="script">Quality Products</h2>
    <div class="photo" role="img" aria-label="Two tequila makers inspecting a glass in a barrel cellar"></div>
    <p>Vestibulum ante ipsum primis in faucibus orci luctus et ultrices posuere cubilia Curae; Ut et scelerisque ante. Donec erat purus, faucibus vitae congue vel, porttitor nec lectus.</p>
    <a href="#">READ MORE</a>
  </article>
  <article class="feature abs" style="left:281px">
    <h2 class="script">Experienced Maker</h2>
    <div class="photo" role="img" aria-label="Two tequila makers tasting from small glasses among barrels"></div>
    <p>Vestibulum ante ipsum primis in faucibus orci luctus et ultrices posuere cubilia Curae; Ut et scelerisque ante. Donec erat purus, faucibus vitae congue vel, porttitor nec lectus.</p>
    <a href="#">READ MORE</a>
  </article>
  <article class="feature abs" style="left:546px">
    <h2 class="script">Production Process</h2>
    <div class="photo" role="img" aria-label="Production video still of makers beside steel distillery equipment" style="background:linear-gradient(110deg,#3a3530,#8a8680 35%,#d9d6d0 60%,#eeeeea)">
      <svg class="play" viewBox="0 0 36 36"><circle cx="18" cy="18" r="17" fill="rgba(255,255,255,.75)"/><path d="M14 10l12 8-12 8z" fill="#555"/></svg>
    </div>
    <p>Vestibulum ante ipsum primis in faucibus orci luctus et ultrices posuere cubilia Curae; Ut et scelerisque ante. Donec erat purus, faucibus vitae congue vel, porttitor nec lectus.</p>
    <a href="#">Watch Full Video</a>
  </article>
</main>

<section class="contact-bar abs">
  <h3 class="quick script abs">Quick Contact</h3>
  <div class="field abs" style="top:43px">Name</div>
  <div class="field abs" style="top:74px">Email</div>
  <div class="field abs" style="top:106px">Phone</div>
  <div class="field abs" style="top:137px;height:63px">Message</div>
  <a class="submit btn abs" href="#">Submit</a>

  <h3 class="news script abs">Latest News</h3>
  <div class="news-item abs" style="top:46px">
    <span class="date">17<small>July</small></span>
    <p>Lorem ipsum dolor sit amet, consectetur adipiscing elit.</p>
    <a href="#">Read More</a>
  </div>
  <div class="news-rule abs"></div>
  <div class="news-item abs" style="top:130px">
    <span class="date">15<small>July</small></span>
    <p>Lorem ipsum dolor sit amet, consectetur adipiscing elit.</p>
    <a href="#">Read More</a>
  </div>

  <h3 class="testi script abs">Testimonials</h3>
  <svg class="quote-mark abs" viewBox="0 0 34 34"><circle cx="17" cy="17" r="17" fill="#2f2f2f"/><text x="8" y="30" font-family="Lora,serif" font-size="26" fill="#888">&#8220;</text></svg>
  <p class="testi-text abs">Lorem ipsum dolor sit amet, consectetur adipiscing elit. Fusce accumsan, elit a suscipit sagittis, tortor sapien cursus risus, non rhoncus lectus nunc ac nulla.....<a href="#">Continue</a></p>
  <p class="author abs">Lena Hartwell<span>Posted on July17, 2012</span></p>
  <div class="avatar abs" role="img" aria-label="Portrait of the reviewer holding a glass"></div>
</section>

<footer>
  <p class="legal abs">©2012 ByVelmaros. All Right Reserved &nbsp;|&nbsp; Privacy Policy</p>
  <div class="social abs"><span></span><span></span><span></span><span></span></div>
</footer>

</body>
</html>
```